Business Card Design

Kestrow Dynamics is an Australian company that provides a new monitoring product for solar systems. We are a tech company that needs a professional, corporate business card. Clean lines, no clutter, easy to read and import into contacts.

Can be double sided or single sided - but only want a simple logo on back

Target Market(s)

Professionals and trades. Business community

Industry/Entity Type

Business

Contact Information for Business Card

See email signature image. We need business cards for 2 people (same design)

Requirements
Must have
• Logo.
Contact details

```html
<!DOCTYPE html>
<html lang="en">
<head>
<meta charset="utf-8">
<title>Kestrow Dynamics – Business Cards</title>
<link href="https://fonts.googleapis.com/css2?family=PT+Sans+Narrow:wght@400;700&display=swap" rel="stylesheet">
<style>
  :root {
    --backdrop: #2b2b2c;
    --card: #ffffff;
    --brand-blue: #2a6db3;
    --brand-gold: #f2ae1c;
    --text-blue: #2a6db3;
  }
  * { box-sizing: border-box; margin: 0; padding: 0; }
  html, body {
    width: 1200px; height: 800px; overflow: hidden;
    background: var(--backdrop);
    font-family: "PT Sans Narrow", "Arial Narrow", sans-serif;
  }
  .canvas {
    width: 1200px; height: 800px;
    display: flex; justify-content: center; align-items: center; gap: 70px;
  }
  .business-card {
    position: relative;
    width: 340px; height: 560px;
    background: var(--card);
    box-shadow: 0 10px 30px rgba(0,0,0,.45);
    padding: 0 30px 0 58px;
    display: flex; flex-direction: column;
  }
  .edge-stripes {
    position: absolute; left: 0; top: 0; bottom: 0;
    display: flex;
  }
  .edge-stripes .stripe-gold { width: 9px; background: var(--brand-gold); }
  .edge-stripes .stripe-gap { width: 3px; background: var(--card); }
  .edge-stripes .stripe-blue { width: 9px; background: var(--brand-blue); }

  .brand {
    margin-top: 70px;
    display: flex; align-items: center; justify-content: center; gap: 10px;
  }
  .brand-mark { width: 26px; height: 26px; background: var(--brand-gold); border-radius: 4px; }
  .brand-name {
    font-weight: 700; font-size: 34px; color: var(--brand-blue);
    letter-spacing: .5px; line-height: 1;
  }

  .person { margin-top: 70px; text-align: center; }
  .person-name {
    font-weight: 700; font-size: 30px; color: var(--text-blue);
    text-transform: uppercase; line-height: 1;
  }
  .person-role {
    margin-top: 4px; font-size: 15px; color: var(--brand-gold);
    text-transform: uppercase; letter-spacing: .3px;
  }

  .contact {
    margin-top: auto; margin-bottom: 56px;
    display: grid; grid-template-columns: auto 1fr;
    column-gap: 12px; row-gap: 3px;
    font-size: 15px; line-height: 1.2;
  }
  .contact dt { color: var(--brand-gold); text-transform: uppercase; text-align: right; }
  .contact dd { color: var(--text-blue); text-align: right; }
</style>
</head>
<body>
<main class="canvas">

  <article class="business-card">
    <div class="edge-stripes"><span class="stripe-gold"></span><span class="stripe-gap"></span><span class="stripe-blue"></span></div>
    <header class="brand">
      <span class="brand-mark"></span>
      <span class="brand-name">Kestrow Dynamics</span>
    </header>
    <section class="person">
      <h1 class="person-name">Maren Holloway</h1>
      <p class="person-role">Managing Director</p>
    </section>
    <dl class="contact">
      <dt>Telephone:</dt><dd>+61 2 5550 1427</dd>
      <dt>Cell:</dt><dd>0400 555 218</dd>
      <dt>Email:</dt><dd>maren@kestrowdynamics.com.au</dd>
      <dt>Website:</dt><dd>www.kestrowdynamics.com.au</dd>
      <dt>Address:</dt><dd>Suite 4/88 Harlow Rd., North Sydney,<br>NSW 2060, Australia</dd>
    </dl>
  </article>

  <article class="business-card">
    <div class="edge-stripes"><span class="stripe-gold"></span><span class="stripe-gap"></span><span class="stripe-blue"></span></div>
    <header class="brand">
      <span class="brand-mark"></span>
      <span class="brand-name">Kestrow Dynamics</span>
    </header>
    <section class="person">
      <h1 class="person-name">Tobias Wrenfield</h1>
      <p class="person-role">Software Development<br>Manager</p>
    </section>
    <dl class="contact">
      <dt>Telephone:</dt><dd>+61 2 5550 1433</dd>
      <dt>Cell:</dt><dd>0400 555 391</dd>
      <dt>Email:</dt><dd>tobias@kestrowdynamics.com.au</dd>
      <dt>Website:</dt><dd>www.kestrowdynamics.com.au</dd>
      <dt>Address:</dt><dd>Suite 4/88 Harlow Rd., North Sydney,<br>NSW 2060, Australia</dd>
    </dl>
  </article>

</main>
</body>
</html>
```